fully distributed
Project: fully distributed
fully distributed  - Information Technology
Creative Brief
Use specific fonts
calibri
Simple
Doug Pelliver
CMO
482 Corwin St , Floor 6 New York NY 10019
doug.pelliver@tulvaro.com
logo only
marcste marcste
on 18 and 19 can you fade the grey a litle so it just looks like a faint color
Xpert Xpert
Sure Sir.
we like some of yr designs can u try the design of 17 with the physical layout of card 2
like what you have started will check each one out
thanks we are looking for stationary too
please add fax number 1 800 937 2584

```html
<!DOCTYPE html>
<html lang="en">
<head>
<meta charset="utf-8">
<title>Tulvaro Business Card</title>
<link href="https://fonts.googleapis.com/css2?family=Carlito:wght@400;700&display=swap" rel="stylesheet">
<style>
  :root {
    --page: #e4e4e4;
    --card: #ffffff;
    --ink: #1c1c1c;
    --red: #e63946;
    --grey-text: #555555;
    --bar-dark: #1a1a1a;
  }
  * { box-sizing: border-box; margin: 0; padding: 0; }
  html, body {
    width: 1200px; height: 799px; overflow: hidden;
    background: var(--page);
    font-family: "Carlito", "Calibri", sans-serif;
    color: var(--ink);
  }
  .stage {
    width: 1200px; height: 799px;
    display: flex; align-items: center; justify-content: center; gap: 40px;
  }
  .card {
    position: relative;
    width: 540px; height: 310px;
    background: linear-gradient(160deg, #ffffff 0%, #f6f6f6 100%);
    border-radius: 18px;
    overflow: hidden;
    box-shadow: 0 2px 10px rgba(0,0,0,0.12);
  }
  .corner-bars { position: absolute; display: flex; gap: 10px; }
  .corner-bars span { display: block; height: 7px; }
  .corner-bars .bar-dark { width: 60px; background: var(--bar-dark); }
  .corner-bars .bar-red { width: 70px; background: var(--red); }
  .corner-bars.top-right { top: 22px; right: 0; }
  .corner-bars.bottom-left { bottom: 22px; left: 0; }
  .corner-bars.bottom-left .bar-red { order: -1; }

  .brand-name {
    display: flex; align-items: center; gap: 8px;
    font-weight: 700; color: var(--ink); line-height: 1;
  }
  .brand-dot { border-radius: 50%; background: var(--ink); }

  /* front */
  .card-front .brand-name {
    position: absolute; left: 50%; top: 50%;
    transform: translate(-50%, -50%);
    font-size: 84px;
  }
  .card-front .brand-dot { width: 20px; height: 20px; }

  /* back */
  .card-back .brand-name { position: absolute; left: 34px; top: 127px; font-size: 48px; }
  .card-back .brand-dot { width: 12px; height: 12px; }
  .divider {
    position: absolute; left: 262px; top: 56px;
    width: 2px; height: 190px; background: var(--red);
  }
  .contact {
    position: absolute; right: 30px; top: 60px;
    text-align: right; font-size: 12.5px; color: var(--grey-text); line-height: 1.45;
  }
  .contact-name { font-size: 22px; color: var(--red); line-height: 1.1; }
  .contact-role { font-size: 14px; color: var(--ink); margin-bottom: 14px; }
  .contact-line { display: flex; justify-content: flex-end; align-items: center; gap: 7px; }
  .contact-icon { width: 13px; height: 13px; flex: none; }
</style>
</head>
<body>
<main class="stage">
  <section class="card card-front" aria-label="Card front">
    <div class="corner-bars top-right"><span class="bar-dark"></span><span class="bar-red"></span></div>
    <div class="brand-name">tulvaro<span class="brand-dot"></span></div>
    <div class="corner-bars bottom-left"><span class="bar-dark"></span><span class="bar-red"></span></div>
  </section>

  <section class="card card-back" aria-label="Card back">
    <div class="corner-bars top-right"><span class="bar-dark"></span><span class="bar-red"></span></div>
    <div class="brand-name">tulvaro<span class="brand-dot"></span></div>
    <div class="divider"></div>
    <div class="contact">
      <div class="contact-name">Doug Pelliver</div>
      <div class="contact-role">CMO</div>
      <div class="contact-line">482 Corwin St , Floor 6
        <svg class="contact-icon" viewBox="0 0 14 14"><circle cx="7" cy="7" r="7" fill="var(--red)"/><path d="M7 3a2.5 2.5 0 0 0-2.5 2.5C4.5 8 7 11 7 11s2.5-3 2.5-5.5A2.5 2.5 0 0 0 7 3z" fill="#fff"/></svg>
      </div>
      <div class="contact-line">New York NY 10019
        <svg class="contact-icon" viewBox="0 0 14 14"><circle cx="7" cy="7" r="7" fill="var(--red)"/><circle cx="7" cy="6" r="2" fill="#fff"/></svg>
      </div>
      <div class="contact-line">+1 212 604 7731
        <svg class="contact-icon" viewBox="0 0 14 14"><circle cx="7" cy="7" r="7" fill="var(--red)"/><path d="M4.5 3.5l1.6 0 .7 2-1 .8a5 5 0 0 0 2.4 2.4l.8-1 2 .7v1.6c-3.5.3-6.8-3-6.5-6.5z" fill="#fff"/></svg>
      </div>
      <div class="contact-line">+1 800 937 2584
        <svg class="contact-icon" viewBox="0 0 14 14"><circle cx="7" cy="7" r="7" fill="var(--red)"/><rect x="4" y="5" width="6" height="4.5" fill="#fff"/><rect x="5" y="3" width="4" height="2" fill="#fff"/></svg>
      </div>
      <div class="contact-line">doug.pelliver@tulvaro.com
        <svg class="contact-icon" viewBox="0 0 14 14"><circle cx="7" cy="7" r="7" fill="var(--red)"/><rect x="3.5" y="4.5" width="7" height="5" fill="#fff"/><path d="M3.5 4.5L7 7.5l3.5-3" stroke="var(--red)" stroke-width="0.8" fill="none"/></svg>
      </div>
    </div>
    <div class="corner-bars bottom-left"><span class="bar-dark"></span><span class="bar-red"></span></div>
  </section>
</main>
</body>
</html>
```